Road Construction Company needs business cards

We would like a new business card designed for our business.

We're a road construction company based in Qld, Australia.

Can the business card please have the following information on it.

Name: Brent Malvoy
Position: General Manager
Phone: 0471 592 304
Email: Brent.malvoy@quendix.com.au
Address: 87 Harrowgate Ave, Pindarra, QLD, 4000
Website: www.quendix.com.au

Visually we'd like the card to be professional and simple.

Attached is our logo.

Our website is www.quendix.com.au

Target Market(s)

Men aged 25-60

Contact Information for Business Card

As listed in project description

Font styles to use
Serif

Requirements
Must have
• Large logo on back of card

```html
<!DOCTYPE html>
<html lang="en">
<head>
<meta charset="utf-8">
<title>Quendix Business Card – Brent Malvoy</title>
<link href="https://fonts.googleapis.com/css2?family=Old+Standard+TT:wght@400;700&display=swap" rel="stylesheet">
<style>
  :root {
    --navy: #0a2240;
    --stripe: #174a7c;
    --white: #ffffff;
    --grey: #9a9a9a;
    --logo-grey: #a3a4a6;
    --brand-blue: #0f55a5;
    --icon-grey: #8d8f92;
    --back-light: #ffffff;
    --back-mid: #d5d6de;
    --back-dark: #7f8596;
  }
  * { margin: 0; padding: 0; box-sizing: border-box; }
  html, body {
    width: 1050px;
    height: 1200px;
    overflow: hidden;
    background: var(--white);
    font-family: "Old Standard TT", "Times New Roman", serif;
  }
  .card-sheet { position: relative; width: 1050px; height: 1200px; }

  /* Front face */
  .card-front {
    position: absolute; left: 0; top: 0;
    width: 1050px; height: 600px;
    background: var(--navy);
  }
  .holder-name {
    position: absolute; left: 0; right: 0; top: 160px;
    text-align: center;
    color: var(--white);
    font-weight: 700;
    font-size: 60px;
    letter-spacing: 1px;
    line-height: 1;
  }
  .holder-role {
    position: absolute; left: 0; right: 0; top: 226px;
    text-align: center;
    color: var(--grey);
    font-size: 44px;
    line-height: 1;
  }
  .contact-list { position: absolute; left: 44px; top: 393px; list-style: none; }
  .contact-item {
    display: flex; align-items: center;
    height: 46px;
    color: var(--white);
    font-size: 26px;
    letter-spacing: -0.3px;
  }
  .contact-icon { width: 32px; height: 32px; margin-right: 16px; flex: none; }
  .front-brand {
    position: absolute; right: 36px; top: 436px;
    text-align: right;
    color: var(--logo-grey);
  }
  .front-brand .brand-name {
    font-weight: 700; font-size: 46px; letter-spacing: 3px; line-height: 1;
  }
  .front-brand .brand-site {
    margin-top: 20px; font-weight: 700; font-size: 24px; line-height: 1;
  }
  .front-stripe {
    position: absolute; left: 0; width: 1050px; height: 16px;
    background: var(--stripe);
  }
  .front-stripe.upper { top: 542px; }
  .front-stripe.lower { top: 567px; }

  /* Back face */
  .card-back {
    position: absolute; left: 0; top: 600px;
    width: 1050px; height: 600px;
  }
  .back-backdrop {
    position: absolute; inset: 0;
    background: linear-gradient(100deg, var(--back-light) 12%, var(--back-mid) 55%, var(--back-dark) 100%);
  }
  .back-brand {
    position: absolute; left: 0; right: 0; top: 252px;
    text-align: center;
    color: var(--brand-blue);
    font-weight: 700;
    font-size: 104px;
    letter-spacing: 8px;
    line-height: 1;
  }
</style>
</head>
<body>
<main class="card-sheet">

  <section class="card-front">
    <h1 class="holder-name">BRENT MALVOY</h1>
    <p class="holder-role">General Manager</p>

    <ul class="contact-list">
      <li class="contact-item">
        <svg class="contact-icon" viewBox="0 0 32 32" aria-hidden="true">
          <path d="M8 3 L12 3 L14 10 L11 12 Q14 19 20 21 L22 18 L29 20 L29 24 Q28 29 23 29 Q4 26 3 8 Q3 3 8 3 Z" fill="none" stroke="var(--icon-grey)" stroke-width="2.4" stroke-linejoin="round"/>
        </svg>
        <span>0471 592 304</span>
      </li>
      <li class="contact-item">
        <svg class="contact-icon" viewBox="0 0 32 32" aria-hidden="true">
          <circle cx="16" cy="16" r="14" fill="none" stroke="var(--icon-grey)" stroke-width="2"/>
          <circle cx="16" cy="16" r="4.5" fill="none" stroke="var(--icon-grey)" stroke-width="2"/>
          <path d="M20.5 12 L20.5 18 Q20.5 21 23 21 Q25 21 25 16 A9 9 0 1 0 20 24" fill="none" stroke="var(--icon-grey)" stroke-width="2"/>
        </svg>
        <span>Brent.malvoy@quendix.com.au</span>
      </li>
      <li class="contact-item">
        <svg class="contact-icon" viewBox="0 0 32 32" aria-hidden="true">
          <path d="M16 30 Q6 19 6 12 A10 10 0 0 1 26 12 Q26 19 16 30 Z" fill="none" stroke="var(--icon-grey)" stroke-width="2.6" stroke-linejoin="round"/>
          <circle cx="16" cy="12" r="3.5" fill="none" stroke="var(--icon-grey)" stroke-width="2.4"/>
        </svg>
        <span>87 Harrowgate Ave, Pindarra, QLD, 4000</span>
      </li>
    </ul>

    <div class="front-brand">
      <div class="brand-name">QUENDIX</div>
      <div class="brand-site">www.quendix.com.au</div>
    </div>

    <div class="front-stripe upper"></div>
    <div class="front-stripe lower"></div>
  </section>

  <section class="card-back">
    <div class="back-backdrop" role="img" aria-label="Decorative background: soft white-to-slate gradient with angular facets"></div>
    <div class="back-brand">QUENDIX</div>
  </section>

</main>
</body>
</html>
```